I need a new business card design for my pharmacy.

I need a business card design. I will include my logo.
The card needs to be readable. I prefer to have my logo on one side along with my website, the other side includes the other information. Please use combination of black, neon green, white, and silver. This needs to catch the eye but yet be clearly visible and legible. Thanks

Industry/Entity Type

Pharmacy

Contact Information for Business Card

It needs to have the following information listed:
Mel's Apothecary Owner/Pharm D.
7134 North Brook Lane
Sioux Falls, SD 57231
Phone 605-318-6207
Fax 605-318-6209
email: mel@melsapothecary-example.com
www.melsapothecary-example.com
Store hours Monday-Friday 8 am- 7 pm
Saturday 8 am- 12 pm
Sunday Closed
Please utilize the colors black, white, and neon green, maybe silver.

Requirements
Must have
• It needs to be easily readable!
Nice to have
• It should catch the eye.
Should not have
• Do not use any other colors except listed: black, neon green, white, & silver.

```html
<!DOCTYPE html>
<html lang="en">
<head>
<meta charset="utf-8">
<title>Mel's Apothecary – Business Cards</title>
<link rel="stylesheet" href="https://fonts.googleapis.com/css2?family=Open+Sans:wght@600&family=Arimo&family=Sorts+Mill+Goudy:ital@1&display=swap">
<style>
  :root {
    --paper: #ffffff;
    --ink: #1f1f1f;
    --lime: #b6d567;
    --leaf: #2aa83a;
    --silver: #b4b4b4;
    --silver-light: #e4e4e4;
    --edge: #4fae6a;
  }
  * { margin: 0; padding: 0; box-sizing: border-box; }
  html, body { width: 1200px; height: 714px; overflow: hidden; background: var(--paper); }
  .sheet { position: relative; width: 1200px; height: 714px; }
  .card { position: absolute; }
  .card svg.shape { position: absolute; left: 0; top: 0; }
  .brand-dot { position: absolute; width: 44px; height: 44px; border-radius: 50%; background: var(--ink); }
  .brand-name {
    position: absolute; font-family: "Open Sans", sans-serif; font-weight: 600;
    color: var(--ink); white-space: nowrap; letter-spacing: -0.5px;
  }
  .pattern-field { position: absolute; }
  .title {
    position: absolute; font-family: "Sorts Mill Goudy", serif; font-style: italic; font-weight: 400;
    color: var(--leaf); white-space: nowrap;
  }
  .info { position: absolute; font-family: "Arimo", sans-serif; color: var(--ink); white-space: nowrap; }
  .info p { height: 20px; }

  /* top pill front */
  .pill-front { left: 2px; top: 41px; width: 587px; height: 281px; }
  .pill-front .brand-dot { left: 71px; top: 116px; }
  .pill-front .brand-name { left: 200px; top: 108px; font-size: 40px; }

  /* top pill back */
  .pill-back { left: 601px; top: 41px; width: 587px; height: 281px; }
  .pill-back .clip { position: absolute; inset: 0 4px 7px 0; border-radius: 140px; overflow: hidden; }
  .pill-back .pattern-field {
    left: 225px; top: 0; width: 360px; height: 220px;
    background: radial-gradient(ellipse at 70% 30%, rgba(180,180,180,.35), rgba(182,213,103,.18) 55%, rgba(255,255,255,0) 80%);
  }
  .pill-back .brand-dot { left: 26px; top: 24px; width: 42px; height: 42px; }
  .pill-back .title { left: 60px; top: 66px; font-size: 31px; }
  .pill-back .address { left: 0; top: 122px; width: 276px; font-size: 15.5px; text-align: center; }
  .pill-back .address p { height: 20.5px; }
  .pill-back .address .web { text-align: left; padding-left: 100px; }
  .pill-back .address .email { text-align: left; padding-left: 215px; }
  .pill-back .hours { left: 325px; top: 123px; font-size: 16px; }
  .pill-back .hours p { height: 19.5px; }

  /* bottom rectangle front */
  .rect-front { left: 9px; top: 394px; width: 567px; height: 316px; }
  .rect-front .brand-dot { left: 68px; top: 143px; width: 46px; height: 46px; }
  .rect-front .brand-name { left: 200px; top: 139px; font-size: 40px; }

  /* bottom rectangle back */
  .rect-back { left: 605px; top: 394px; width: 567px; height: 316px; }
  .rect-back .face {
    position: absolute; inset: 0 4px 6px 0; background: var(--paper);
    border: 1px solid var(--edge); border-radius: 9px; overflow: hidden;
    box-shadow: 4px 5px 0 var(--silver);
  }
  .rect-back .pattern-field {
    left: 200px; top: 0; width: 365px; height: 150px;
    background: radial-gradient(ellipse at 70% 35%, rgba(180,180,180,.35), rgba(182,213,103,.18) 55%, rgba(255,255,255,0) 80%);
  }
  .rect-back .brand-dot { left: 483px; top: 18px; width: 46px; height: 46px; }
  .rect-back .title { left: 28px; top: 80px; font-size: 32px; }
  .rect-back .address { left: 27px; top: 147px; font-size: 16px; }
  .rect-back .address p { height: 20.6px; }
  .rect-back .hours { left: 301px; top: 148px; font-size: 17px; }
  .rect-back .hours p { height: 20.3px; }
</style>
</head>
<body>
<main class="sheet">

  <section class="card pill-front">
    <svg class="shape" width="587" height="281" viewBox="0 0 587 281">
      <defs>
        <clipPath id="pill-front-clip"><rect x="0" y="0" width="581" height="273" rx="136"/></clipPath>
      </defs>
      <rect x="4" y="6" width="581" height="273" rx="136" fill="var(--silver)"/>
      <rect x="0" y="0" width="581" height="273" rx="136" fill="var(--paper)" stroke="var(--silver-light)"/>
      <rect x="174" y="0" width="420" height="273" fill="var(--lime)" clip-path="url(#pill-front-clip)"/>
      <path d="M463 30 C505 38 545 70 547 100 C530 78 500 55 463 30 Z" fill="var(--paper)"/>
      <line x1="176" y1="102" x2="176" y2="186" stroke="var(--ink)" stroke-width="2"/>
    </svg>
    <span class="brand-dot" aria-hidden="true"></span>
    <span class="brand-name">Mel's Apothecary</span>
  </section>

  <section class="card pill-back">
    <svg class="shape" width="587" height="281" viewBox="0 0 587 281">
      <rect x="4" y="7" width="581" height="272" rx="136" fill="var(--silver)"/>
      <rect x="0.5" y="0.5" width="581" height="272" rx="136" fill="var(--paper)" stroke="var(--silver-light)"/>
    </svg>
    <div class="clip">
      <div class="pattern-field" role="img" aria-label="Faint scattered pattern of grey capsule outlines and green dots"></div>
    </div>
    <span class="brand-dot" aria-hidden="true"></span>
    <h1 class="title">Mel's Apothecary Owner/Pharm D.</h1>
    <div class="info address">
      <p>7134 North Brook Lane</p>
      <p>Sioux Falls, SD 57231</p>
      <p>Phone 605-318-6207</p>
      <p>Fax 605-318-6209</p>
      <p class="web">www.melsapothecary-example.com</p>
      <p class="email">email: mel@melsapothecary-example.com</p>
    </div>
    <div class="info hours">
      <p>Store hours Monday-Friday</p>
      <p>8 am- 7 pm</p>
      <p>Saturday 8 am- 12 pm</p>
      <p>Sunday Closed</p>
    </div>
  </section>

  <section class="card rect-front">
    <svg class="shape" width="567" height="316" viewBox="0 0 567 316">
      <defs>
        <clipPath id="rect-front-clip"><rect x="0" y="0" width="563" height="309" rx="9"/></clipPath>
      </defs>
      <rect x="4" y="6" width="563" height="309" rx="9" fill="var(--silver)"/>
      <rect x="0.5" y="0.5" width="562" height="308" rx="9" fill="var(--paper)" stroke="var(--edge)"/>
      <path d="M180 95 C180 40 300 10 563 2 L563 306 C330 305 185 300 178 215 Z" fill="var(--lime)" clip-path="url(#rect-front-clip)"/>
      <path d="M205 55 C230 30 275 18 310 15 C270 28 240 40 205 55 Z" fill="var(--paper)"/>
      <line x1="180" y1="120" x2="180" y2="200" stroke="var(--ink)" stroke-width="2"/>
    </svg>
    <span class="brand-dot" aria-hidden="true"></span>
    <span class="brand-name">Mel's Apothecary</span>
  </section>

  <section class="card rect-back">
    <div class="face">
      <div class="pattern-field" role="img" aria-label="Faint scattered pattern of grey capsule outlines and green dots"></div>
    </div>
    <span class="brand-dot" aria-hidden="true"></span>
    <h1 class="title">Mel's Apothecary Owner/Pharm D.</h1>
    <div class="info address">
      <p>7134 North Brook Lane</p>
      <p>Sioux Falls, SD 57231</p>
      <p>&nbsp;Phone 605-318-6207</p>
      <p>&nbsp;Fax 605-318-6209</p>
      <p>&nbsp;www.melsapothecary-example.com</p>
      <p>&nbsp;&nbsp;email: mel@melsapothecary-example.com</p>
    </div>
    <div class="info hours">
      <p>Store hours Monday-Friday</p>
      <p>8 am- 7 pm</p>
      <p>Saturday 8 am- 12 pm</p>
      <p>Sunday Closed</p>
    </div>
  </section>

</main>
</body>
</html>
```